依頼詳細
某ホテルのブライダルフェアや内覧会(結婚が決まったカップルが衣装や引き出物などを選ぶイベント)などでお客様に配布します。お客様にこのチラシを見せながら内容を説明したりもするので、わかりやすい料金とコース内容が伝えられるデザインをお願いします。
記載項目
屋号/電話番号/料金プラン/なにか良いキャッチフレーズなどあればお願いしたいです。
サイズ
A4
ページ数
片面
希望イメージ
シンプル 複雑
単色 カラフル
暗い 明るい
日常 高級
遊び心 厳粛
未来的 伝統的
女性的 男性的
希望する色
オレンジ、緑など「新鮮」「明るい」イメージ色を希望します。
納品ファイル
• イラストレーター形式 (.ai)
• フォトショップ形式 (.psd)
補足説明
いままでは市販のワープロソフトなどで付属のテンプレートなどを元に作ってきましたが、
やはりプロの広告を出している他社と大きく差がついてしまっています。 もう自分でデザインしていては他社と差が広がるばかりと感じ、今回依頼させていただきます。よろしくお願いいたします。
当方の使用していたチラシです
遅れてすみませんでした。映っている本人たちに許可は取りました。よろしくお願いいたします。
■ 選んだ理由

最終的にお二方の提案を残させていただきましたが、通り過ぎるようとするお客様の目を止まらせ、それでいて優先される物が目立ち、シンプルにまとまっていてちょっとポップな感じで同ビデオ業者との差別化をはかっているこの提案を選ばせていただきました。

■ 提案者全員のお礼・コメント

この度は当方の依頼に対して、予想以上に多くのクリエーターの方々から、想像以上にハイクオリティーな提案を多数いただき心から感謝しております。
本当にどれを選んで良い物かかなり悩みました。改めてこのサイトの素晴らしさを実感いたしました。次回また商品内容を変える際には間違いなくここに依頼させていただきます。
提案を下さったすべてのクリエーターの皆様に感謝申し上げます。
ありがとうございました。

```html
<!DOCTYPE html>
<html lang="ja">
<head>
<meta charset="UTF-8">
<title>Memorial Video — Creation Studio PRISM</title>
<link href="https://fonts.googleapis.com/css2?family=Noto+Sans+JP:wght@400;500;700;900&family=Great+Vibes&family=Noto+Serif+JP:wght@600&display=swap" rel="stylesheet">
<style>
:root{
  --yellow:#f6d21a;
  --ink:#1d1d1d;
  --price:#e2401b;
  --heading:#2a2a2a;
  --white:#ffffff;
  --rule:#111111;
}
*{margin:0;padding:0;box-sizing:border-box}
html,body{width:849px;height:1200px;overflow:hidden;background:var(--white)}
body{font-family:"Noto Sans JP",sans-serif;color:var(--ink)}
.flyer{position:relative;width:849px;height:1200px;background:var(--yellow);border:6px solid var(--rule)}
.hero{position:absolute;left:14px;top:14px;width:809px;height:545px;
  background:radial-gradient(ellipse at 30% 25%,#fff6d8 0%,#d9b877 22%,#7d5a34 50%,#3b2a1c 80%),#3b2a1c;}
.hero-catch{position:absolute;left:14px;top:420px;width:560px;height:46px;background:rgba(20,14,8,.7);
  color:var(--white);font-family:"Noto Serif JP",serif;font-weight:600;font-size:27px;line-height:46px;padding-left:36px;letter-spacing:1px}
.hero-title{position:absolute;left:40px;top:455px;font-family:"Great Vibes",cursive;color:var(--white);font-size:104px;line-height:1;
  text-shadow:0 2px 6px rgba(0,0,0,.6)}
.hero-venue{position:absolute;right:20px;top:540px;background:var(--white);color:var(--ink);font-family:"Noto Serif JP",serif;
  font-size:17px;letter-spacing:1px;padding:4px 14px;border:2px solid var(--rule)}
.sec-title{font-weight:900;font-size:27px;line-height:1.2;color:var(--heading);letter-spacing:-.5px}
.left{position:absolute;left:30px;top:590px;width:385px}
.lead{font-size:13px;line-height:1.5;margin-top:8px}
.couple{position:absolute;left:0;top:92px;width:170px;height:240px;background:linear-gradient(160deg,#f3e6d8,#c9a98a 60%,#8c6e55);border:3px solid var(--white)}
.plans{position:absolute;left:180px;top:88px;width:205px}
.plan{margin-bottom:6px}
.plan-name{font-weight:700;font-size:17px;line-height:1.3}
.plan-name::before{content:"■";color:var(--price);margin-right:2px}
.plan-row{display:flex;align-items:baseline;justify-content:space-between;padding-left:6px;height:26px}
.plan-row span{font-size:10px}
.plan-row b{color:var(--price);font-size:21px;font-weight:900;line-height:1}
.plan-row b small{font-size:10px;font-weight:500;color:var(--ink)}
.option{position:absolute;left:30px;top:955px;width:385px}
.option-title{font-weight:900;font-size:30px;line-height:1.2;color:var(--heading)}
.opt{display:flex;justify-content:space-between;align-items:baseline;font-weight:700;font-size:17px;margin-top:4px}
.opt b{color:var(--price);font-size:21px;font-weight:900}
.opt b small{font-size:11px;color:var(--ink);font-weight:500}
.opt-note{font-size:11px;line-height:1.3}
.right{position:absolute;left:425px;top:590px;width:395px}
.film{position:absolute;left:0;top:80px;width:150px;height:345px;background:#151515}
.film-frames{position:absolute;inset:10px 22px;background:linear-gradient(180deg,#d8b590,#7a5b3d 30%,#e6d3c0 55%,#b48d63 80%,#5a412b)}
.right-copy{position:absolute;left:165px;top:82px;width:225px;font-size:14px;line-height:1.55}
.right-price{position:absolute;left:165px;top:250px;width:225px}
.right-price .label{font-weight:700;font-size:16px}
.right-price b{display:block;color:var(--price);font-size:30px;font-weight:900;line-height:1.1}
.right-price b small{font-size:12px;color:var(--ink);font-weight:500}
.set-note{font-size:13px;font-weight:700;margin-top:6px;line-height:1.4}
.studio{position:absolute;left:425px;top:1025px;width:395px;height:150px;background:var(--white);border:3px solid var(--rule);padding:8px 14px}
.studio-name{font-weight:900;font-size:29px;line-height:1.1}
.studio-kana{font-size:13px}
.studio-tel{font-weight:900;font-size:27px;margin-top:2px}
.studio-note{font-size:10px;line-height:1.35;margin-top:3px}
</style>
</head>
<body>
<div class="flyer">
  <div class="hero" role="img" aria-label="チャペルのシャンデリアの下で挙式する新郎新婦の写真"></div>
  <div class="hero-catch">感動の瞬間を高品質な映像で</div>
  <div class="hero-title">Memorial Video</div>
  <div class="hero-venue">HOTEL LUMIÈRE GARDEN</div>

  <section class="left">
    <h2 class="sec-title">挙式披露宴メモリアルビデオ</h2>
    <p class="lead">「生涯一度の大切な瞬間」を経験豊富なプロのカメラマンが心を込めて撮影し、美しい映像に仕上げます。</p>
    <div class="couple" role="img" aria-label="笑顔の新郎新婦の写真"></div>
    <div class="plans">
      <div class="plan"><div class="plan-name">挙式のみ</div>
        <div class="plan-row"><span>メニューなし</span><b>60,900円<small>(税込)</small></b></div>
        <div class="plan-row"><span>メニューあり</span><b>76,650円<small>(税込)</small></b></div></div>
      <div class="plan"><div class="plan-name">披露宴のみ</div>
        <div class="plan-row"><span>メニューなし</span><b>105,000円<small>(税込)</small></b></div>
        <div class="plan-row"><span>メニューあり</span><b>131,250円<small>(税込)</small></b></div></div>
      <div class="plan"><div class="plan-name">挙式＋披露宴</div>
        <div class="plan-row"><span>メニューなし</span><b>136,500円<small>(税込)</small></b></div>
        <div class="plan-row"><span>メニューあり</span><b>162,750円<small>(税込)</small></b></div></div>
    </div>
  </section>

  <section class="option">
    <h3 class="option-title">OPTION</h3>
    <div class="opt">ハイビジョン仕上げ<b>52,500円<small>(税込)</small></b></div>
    <p class="opt-note">高画質HD映像をブルーレイに記録します。</p>
    <div class="opt">外式出張サービス<b>10,500円<small>(税込)</small></b></div>
    <p class="opt-note">当ホテル以外の教会、神社での挙式を撮影します。</p>
    <div class="opt">ディスクコピー<b>10,500円<small>(税込)</small></b></div>
    <p class="opt-note">本編商品の複製品を作成します。</p>
  </section>

  <section class="right">
    <h2 class="sec-title">撮って出し<br>エンドロールムービー</h2>
    <div class="film"><div class="film-frames" role="img" aria-label="挙式の場面を並べたフィルムストリップ写真"></div></div>
    <p class="right-copy">おふたりのイメージ映像や舞台裏など当日の様子を多彩なカットで編集し、披露宴の最後にエンドロールとして上映します。</p>
    <div class="right-price">
      <div class="label">単品</div>
      <b>136,500円<small>(税込)</small></b>
      <p class="set-note">「挙式披露宴メモリアルビデオ」とセットなら</p>
      <div class="label">プラス</div>
      <b>78,750円<small>(税込)</small></b>
    </div>
  </section>

  <div class="studio">
    <div class="studio-name">Creation Studio PRISM</div>
    <div class="studio-kana">(クリエーション・スタジオ・プリズム)</div>
    <div class="studio-tel">TEL/FAX 012-345-6789</div>
    <p class="studio-note">※撮影・編集費用の詳細はお気軽にお問い合わせください。会場の状況により撮影内容が変わる場合があります。</p>
  </div>
</div>
</body>
</html>
```